Thistle Root Organic

Please find attached screenshots of a same product as what I'm selling, looking for similar packaging but yet a whole new different design with my own logo rivertiles which is also attached. It will be on white bags with the clear on the bottom center. As far as colors maby green yellow and black or if you have a better idea. Also it needs to be something that looks up to date modern I like when it has that two-tone gloss to it where it goes from darker to lighter.

```html
<!DOCTYPE html>
<html lang="en">
<head>
<meta charset="utf-8">
<title>Thistle Root Organic – Pouch Front</title>
<link href="https://fonts.googleapis.com/css2?family=Montserrat:wght@600;800&family=Oswald:wght@500&display=swap" rel="stylesheet">
<style>
  :root{
    --stage:#6b6b6b;
    --bag-white:#f7f8f6;
    --ink:#111512;
    --ink-soft:#2c322e;
    --forest:#0f5a2f;
    --green:#2f9a46;
    --lime:#9ccc3a;
    --yellow:#f2d22e;
    --window-tint:#e4ebe2;
    --white:#ffffff;
  }
  *{box-sizing:border-box;}
  html,body{margin:0;padding:0;overflow:hidden;}
  body{width:1200px;height:1118px;background:var(--stage);position:relative;font-family:"Montserrat",sans-serif;}

  .front-panel{
    position:absolute;left:320px;top:119px;width:560px;height:880px;
    background:var(--bag-white);overflow:hidden;
  }

  /* top gloss band: black to lighter charcoal */
  .top-band{
    position:absolute;left:0;top:0;width:100%;height:170px;
    background:linear-gradient(160deg,var(--ink) 0%,var(--ink) 48%,var(--ink-soft) 52%,#3d4540 100%);
    display:flex;align-items:center;justify-content:space-between;padding:0 40px;
  }
  .brand{display:flex;align-items:center;gap:14px;}
  .brand-dot{width:34px;height:34px;border-radius:50%;background:var(--lime);}
  .brand-name{font-weight:800;font-size:30px;color:var(--white);letter-spacing:1px;}
  .organic-seal{
    width:104px;height:104px;border-radius:50%;
    background:var(--yellow);color:var(--ink);
    display:flex;flex-direction:column;align-items:center;justify-content:center;text-align:center;
  }
  .organic-seal .pct{font-weight:800;font-size:22px;line-height:1;}
  .organic-seal .word{font-weight:800;font-size:15px;line-height:1.2;text-transform:uppercase;}
  .organic-seal .sub{font-weight:600;font-size:8px;letter-spacing:1px;text-transform:uppercase;}

  /* title block */
  .title-block{position:absolute;left:0;top:206px;width:100%;text-align:center;}
  .tagline{margin:0;font-weight:600;font-size:17px;letter-spacing:6px;color:var(--green);text-transform:uppercase;}
  .product-name{margin:10px 0 0;font-weight:800;font-size:68px;line-height:1;color:var(--ink);letter-spacing:-1px;}
  .product-kind{margin:8px 0 0;font-weight:800;font-size:24px;letter-spacing:10px;color:var(--green);text-transform:uppercase;}

  /* lower gloss sweep: green to yellow */
  .gloss-sweep{
    position:absolute;left:0;top:430px;width:100%;height:450px;
    background:linear-gradient(135deg,var(--forest) 0%,var(--green) 45%,var(--lime) 75%,var(--yellow) 100%);
    clip-path:polygon(0 18%,100% 0,100% 100%,0 100%);
  }
  .gloss-sweep::after{
    content:"";position:absolute;inset:0;
    background:linear-gradient(160deg,rgba(255,255,255,.22) 0%,rgba(255,255,255,.22) 40%,rgba(255,255,255,0) 41%);
  }

  /* clear window, bottom centre */
  .clear-window{
    position:absolute;left:150px;top:540px;width:260px;height:230px;border-radius:130px 130px 24px 24px;
    background:linear-gradient(180deg,var(--window-tint) 0%,#cdd8c6 100%);
    border:4px solid var(--white);
  }

  .weight-strip{
    position:absolute;left:0;bottom:0;width:100%;height:66px;background:var(--ink);
    display:flex;align-items:center;justify-content:center;
  }
  .net-weight{font-family:"Oswald",sans-serif;font-weight:500;font-size:18px;color:var(--white);letter-spacing:1px;}
</style>
</head>
<body>
  <main class="front-panel">
    <header class="top-band">
      <div class="brand">
        <div class="brand-dot"></div>
        <span class="brand-name">rivertiles</span>
      </div>
      <div class="organic-seal">
        <span class="pct">100%</span>
        <span class="word">Organic</span>
        <span class="sub">Quality Food</span>
      </div>
    </header>

    <section class="title-block">
      <p class="tagline">Herbs for Wellness</p>
      <h1 class="product-name">Thistle Root</h1>
      <p class="product-kind">Organic</p>
    </section>

    <div class="gloss-sweep"></div>
    <div class="clear-window" role="img" aria-label="Clear window showing the dried root inside the bag"></div>

    <footer class="weight-strip"><span class="net-weight">NET WT. 1.27 OZ. (36g)</span></footer>
  </main>
</body>
</html>
```